Flyer for Aluminium recycling business

We are a startup aluminium recycling business. We don’t have a logo yet. I’ve attached a flyer created by one of our sales people but it’s a bit average and we need something a bit more modern and slick. You have creative license to completely change everything - as long as the information being communicated is the same.

Target Market(s)

Hospitality, Hotels, Apartment blocks, malls etcs

Industry/Entity Type

Aluminium recycling

Requirements
Must have
• the wording
Nice to have
• you have free license on design aspect

```html
<!DOCTYPE html>
<html lang="en">
<head>
<meta charset="utf-8">
<title>Circular Reclaim – Aluminium Recycling Flyer</title>
<link rel="stylesheet" href="https://fonts.googleapis.com/css2?family=Poppins:wght@400;700;800&family=Roboto:wght@400&display=swap">
<style>
  :root {
    --backdrop: #808080;
    --paper: #ffffff;
    --forest: #273f3a;
    --amber: #fbb61f;
    --ink-soft: #5c5c5c;
    --text-light: #ffffff;
  }
  * { margin: 0; padding: 0; box-sizing: border-box; }
  html, body { width: 1200px; height: 1200px; overflow: hidden; background: var(--backdrop); }
  .flyer {
    position: absolute; left: 234px; top: 86px; width: 739px; height: 1036px;
    background: var(--paper); font-family: "Roboto", sans-serif;
  }
  .masthead { position: absolute; left: 0; top: 0; width: 100%; height: 125px; background: var(--forest); }
  .brand-name {
    position: absolute; left: 0; top: 30px; width: 100%; text-align: center;
    font-family: "Poppins", sans-serif; font-weight: 800; font-size: 57px;
    letter-spacing: 1px; word-spacing: 10px; color: var(--text-light); line-height: 1.2;
  }
  .tagline {
    position: absolute; left: 41px; top: 106px; width: 657px; height: 41px;
    background: var(--amber); border: 2px solid var(--forest); border-radius: 6px;
    font-family: "Poppins", sans-serif; font-weight: 700; font-size: 22.5px;
    color: var(--forest); text-align: center; line-height: 37px;
  }
  .intro {
    position: absolute; left: 0; top: 164px; width: 100%; text-align: center;
    font-size: 21px; line-height: 27px; color: var(--ink-soft);
  }
  .panel { position: absolute; left: 63px; width: 614px; background: var(--forest); border-radius: 12px; }
  .panel-steps { top: 268px; height: 270px; }
  .panel-accepted { top: 562px; height: 315px; }
  .panel-tab { position: absolute; top: 0; }
  .panel-tab svg { display: block; }
  .panel-tab span {
    position: absolute; left: 0; top: 0; width: 100%; text-align: center;
    font-family: "Poppins", sans-serif; font-weight: 700; font-size: 24px;
    line-height: 36px; color: var(--forest);
  }
  .checklist { position: absolute; left: 23px; right: 20px; list-style: none; }
  .panel-steps .checklist { top: 54px; }
  .panel-accepted .checklist { top: 62px; }
  .checklist li {
    position: relative; padding-left: 25px; margin-bottom: 10.5px;
    font-size: 16.8px; line-height: 19.5px; color: var(--text-light);
  }
  .checklist li svg { position: absolute; left: 0; top: 3px; }
  .contact-phone {
    position: absolute; left: 0; top: 912px; width: 100%;
    display: flex; justify-content: center; align-items: center; gap: 12px;
    font-family: "Poppins", sans-serif; font-weight: 700; font-size: 39px; color: var(--forest);
  }
  .contact-email {
    position: absolute; left: 0; top: 969px; width: 100%;
    display: flex; justify-content: center; align-items: center; gap: 15px;
    font-family: "Poppins", sans-serif; font-weight: 400; font-size: 21px; color: var(--forest);
  }
</style>
</head>
<body>
<svg width="0" height="0" style="position:absolute">
  <defs>
    <symbol id="tick" viewBox="0 0 14 14">
      <circle cx="7" cy="7" r="7" fill="#fbb61f"/>
      <path d="M3.8 7.2 L6.1 9.4 L10.3 4.8" fill="none" stroke="#273f3a" stroke-width="1.8" stroke-linecap="round" stroke-linejoin="round"/>
    </symbol>
  </defs>
</svg>

<main class="flyer">
  <header class="masthead">
    <h1 class="brand-name">CIRCULAR RECLAIM</h1>
  </header>
  <p class="tagline">Playing the fair aluminium recycling game for good</p>
  <p class="intro">Our partnership with you is based on common sense,<br>mutual gain and a better tomorrow</p>

  <section class="panel panel-steps">
    <div class="panel-tab" style="left:217px;width:178px;">
      <svg width="178" height="42" viewBox="0 0 178 42">
        <path d="M1 0 L177 0 L151 36 Q147 41 140 41 L38 41 Q31 41 27 36 Z" fill="#fbb61f" stroke="#ffffff" stroke-width="2"/>
      </svg>
      <span>It's simple</span>
    </div>
    <ul class="checklist">
      <li><svg width="14" height="14"><use href="#tick"/></svg>We bring you a free bin</li>
      <li><svg width="14" height="14"><use href="#tick"/></svg>You throw all and any aluminium waste into the bin - no need to super-clean it. Try to compact/squash the aluminium as much as possible</li>
      <li><svg width="14" height="14"><use href="#tick"/></svg>We collect the bin at no charge</li>
      <li><svg width="14" height="14"><use href="#tick"/></svg>We turn the aluminium waste into a desirable resource</li>
      <li><svg width="14" height="14"><use href="#tick"/></svg>We pay you for however much of that resource your waste has generated - and give you a report on that, so you can see how good you are</li>
    </ul>
  </section>

  <section class="panel panel-accepted">
    <div class="panel-tab" style="left:93px;width:427px;">
      <svg width="427" height="42" viewBox="0 0 427 42">
        <path d="M1 0 L426 0 L401 36 Q397 41 390 41 L38 41 Q31 41 27 36 Z" fill="#fbb61f" stroke="#ffffff" stroke-width="2"/>
      </svg>
      <span>Examples of what we can take</span>
    </div>
    <ul class="checklist">
      <li><svg width="14" height="14"><use href="#tick"/></svg>Used beverage cans - any</li>
      <li><svg width="14" height="14"><use href="#tick"/></svg>Tinfoil-scrunched, crusty, burned or dirty</li>
      <li><svg width="14" height="14"><use href="#tick"/></svg>Disposable BBQ roasting trays</li>
      <li><svg width="14" height="14"><use href="#tick"/></svg>Aluminium takeaway containers</li>
      <li><svg width="14" height="14"><use href="#tick"/></svg>Wine bottle screw tops (and collars - if you can get them off)</li>
      <li><svg width="14" height="14"><use href="#tick"/></svg>Brewmatic (or any other aluminium) coffee pods</li>
      <li><svg width="14" height="14"><use href="#tick"/></svg>Tear-off can lids</li>
      <li><svg width="14" height="14"><use href="#tick"/></svg>Old/broken Slate-Pads, tablets, laptops or cell phones</li>
    </ul>
  </section>

  <footer>
    <p class="contact-phone">
      <svg width="32" height="32" viewBox="0 0 32 32" aria-hidden="true">
        <circle cx="16" cy="16" r="16" fill="#fbb61f"/>
        <path d="M10.5 8.5 L13.5 8 L15 12 L13 13.8 Q14.5 17.5 18.2 19 L20 17 L24 18.5 L23.5 21.5 Q22.5 23.5 20 23.3 Q10 21.5 8.7 12 Q8.5 9.5 10.5 8.5 Z" fill="#273f3a"/>
      </svg>
      021 555 0148
    </p>
    <p class="contact-email">
      <svg width="22" height="16" viewBox="0 0 22 16" aria-hidden="true">
        <rect x="0" y="0" width="22" height="16" rx="1.5" fill="#273f3a"/>
        <path d="M1 1.5 L11 9 L21 1.5" fill="none" stroke="#ffffff" stroke-width="1.6"/>
      </svg>
      join@circularreclaim.co.nz
    </p>
  </footer>
</main>
</body>
</html>
```